Landing Page - #1 Social Media Training

I need a landing page where i'm going to sell the number one social media for small business package. Hopefully i can use this template for others.

The themes are in oranges.

See www.tavuvkip.com

Its a dogs breakfast.

I need high end, good looking, kova/trindlepay/logos.
Would love a wordpress design but i could slice it into one if it wasn't.

Need room for feature bullet points, a video preview, and text along the bottom... Want it in oranges and whites like the packaging with social media along the top... Side bar on the right for opt-in box, left side copy etc.

Target Market(s)

The audience is small and medium businesses.

Industry/Entity Type

Small Business

Requirements
Must have
• Opt-in
headline
footer

```html
<!DOCTYPE html>
<html lang="en">
<head>
<meta charset="utf-8">
<title>nuvora — Social Media &amp; Internet Marketing</title>
<link href="https://fonts.googleapis.com/css2?family=Roboto:wght@400;500;700&family=Crimson+Text:ital,wght@0,600;1,400&display=swap" rel="stylesheet">
<style>
  :root {
    --orange: #f08323;
    --orange-deep: #e8690f;
    --orange-light: #fba54a;
    --text-grey: #6f7173;
    --text-dark: #555759;
    --link-blue: #4a77a0;
    --head-blue: #3e6a92;
    --band-top: #f3f3f4;
    --band-bottom: #dcdcde;
    --band-border: #b9babc;
    --panel: #9a9d9f;
    --panel-dark: #85888a;
    --video: #4d4d4d;
    --price-blue: #2d5fc0;
    --page: #ececec;
    --white: #ffffff;
  }
  * { box-sizing: border-box; margin: 0; padding: 0; }
  html, body { width: 1200px; height: 1008px; overflow: hidden; }
  body {
    position: relative;
    background: radial-gradient(ellipse at 50% 0%, #ffffff 0%, #f2f2f2 35%, var(--page) 100%);
    font-family: "Roboto", Arial, sans-serif;
    color: var(--text-grey);
  }
  .brand {
    position: absolute; left: 208px; top: 42px;
    font-size: 52px; font-weight: 700; letter-spacing: -1px;
    color: var(--orange); line-height: 1;
  }
  .brand-tag {
    position: absolute; left: 212px; top: 100px;
    font-size: 15px; color: var(--link-blue);
  }
  .payments { position: absolute; top: 60px; right: 208px; display: flex; gap: 26px; }
  .pay-badge {
    width: 52px; height: 34px; border-radius: 3px;
    background: linear-gradient(#ffffff, #e9e9e9);
    box-shadow: 0 2px 3px rgba(0,0,0,.25);
    display: flex; align-items: center; justify-content: center;
    font-size: 10px; font-weight: 700; color: var(--link-blue);
  }
  .pay-badge.pellmo { margin-left: 18px; background: linear-gradient(#ffffff, #fde7c4); }
  .band {
    position: absolute; left: 200px; width: 792px;
    background: linear-gradient(var(--band-top), var(--band-bottom));
    border: 1px solid var(--band-border);
    text-align: center;
  }
  .headline-band { top: 141px; height: 85px; }
  .headline-band h1 {
    height: 51px; line-height: 52px; font-size: 27px; font-weight: 700; color: var(--text-grey);
    border-bottom: 1px solid #fafafa; box-shadow: 0 1px 0 #c8c9cb;
  }
  .headline-band p { line-height: 33px; font-size: 18px; color: var(--text-grey); }
  .product-box {
    position: absolute; left: 276px; top: 257px; width: 203px; height: 338px;
    background: linear-gradient(100deg, #d9dadc 0%, #d9dadc 13%, #f4f4f5 14%, #e6e7e8 100%);
    box-shadow: 0 8px 10px rgba(0,0,0,.15);
  }
  .pitch { position: absolute; left: 217px; top: 607px; width: 380px; }
  .pitch h2 { font-size: 14px; font-weight: 700; color: var(--head-blue); }
  .features {
    margin-top: 11px; list-style: none;
    display: grid; grid-template-columns: 191px 180px; grid-auto-flow: column; grid-template-rows: repeat(4, 17.5px);
    font-size: 12px; color: var(--link-blue);
  }
  .features li::before { content: "• "; }
  .includes {
    position: absolute; left: 216px; top: 716px; width: 377px; height: 26px;
    background: linear-gradient(#8e9193, #626567);
    border: 1px solid #4f5254;
    color: #fff; font-size: 11.5px; line-height: 24px; text-align: center;
  }
  .includes strong { font-weight: 700; }
  .optin {
    position: absolute; left: 608px; top: 258px; width: 385px; height: 485px;
    background: linear-gradient(128deg, #b2b5b7 0%, #a4a7a9 45%, #8c8f91 45.2%, var(--panel-dark) 100%);
    border: 1px solid #6c6f71;
  }
  .video {
    position: absolute; left: 16px; top: 24px; width: 352px; height: 260px;
    background: var(--video); border: 1px solid #2e2e2e;
    display: flex; align-items: center; justify-content: center;
    font-size: 23px; font-weight: 700; color: #b5b6b7;
  }
  .field {
    position: absolute; left: 16px; width: 352px; height: 35px;
    background: linear-gradient(#fafafa, #e7e7e7); border: 1px solid #77797b;
    font-family: inherit; font-size: 15px; color: #999; padding-left: 12px; line-height: 33px;
  }
  .field.name { top: 308px; }
  .field.email { top: 350px; }
  .buy {
    position: absolute; left: 16px; top: 416px; width: 352px; height: 35px;
    background: linear-gradient(var(--orange-light), var(--orange-deep));
    border: 1px solid #c85a0c;
    color: #fff; font-size: 15px; font-weight: 700; line-height: 33px; text-align: center;
  }
  .price { position: absolute; left: 286px; top: 388px; width: 82px; height: 82px; }
  .price text { font-family: "Roboto", Arial, sans-serif; font-weight: 700; }
  .note { position: absolute; left: 17px; top: 461px; font-size: 11px; color: #fff; }
  .testimonial { position: absolute; left: 200px; top: 774px; width: 792px; text-align: center; font-family: "Crimson Text", Georgia, serif; }
  .testimonial blockquote { font-style: italic; font-size: 21.5px; line-height: 30px; color: #858789; }
  .testimonial cite { display: block; margin-top: 1px; font-style: normal; font-weight: 600; font-size: 21px; color: #7b7d7f; }
  .footer-band { top: 899px; height: 44px; font-size: 22px; line-height: 42px; color: var(--text-grey); }
  .copyright { position: absolute; right: 208px; top: 972px; font-size: 10.5px; color: #8a8c8e; }
</style>
</head>
<body>
  <header>
    <div class="brand">nuvora</div>
    <div class="brand-tag">social growth kits</div>
    <div class="payments">
      <div class="pay-badge">kova</div>
      <div class="pay-badge">trindlepay</div>
      <div class="pay-badge pellmo">pellmo</div>
    </div>
  </header>

  <section class="band headline-band">
    <h1>Social Media &amp; Internet Marketing</h1>
    <p>for Today’s Small to Medium Business</p>
  </section>

  <div class="product-box" role="img" aria-label="Product packaging: Summit Start 101 DVD set by Dale Marrow"></div>

  <section class="pitch">
    <h2>One easy system to help grow your business online!</h2>
    <ul class="features">
      <li>Search Engine Marketing</li>
      <li>Social Media Marketing</li>
      <li>Social Network Marketing</li>
      <li>Internet Marketing</li>
      <li>Applications</li>
      <li>Social Tools</li>
      <li>Community Development</li>
    </ul>
  </section>
  <div class="includes">Includes: <strong>4 DVDs &amp; a Step-by-Step “Do It Yourself” Workbook</strong></div>

  <aside class="optin">
    <div class="video">Video Content</div>
    <div class="field name">Your Name</div>
    <div class="field email">Your Email Address</div>
    <div class="buy">Buy Now</div>
    <svg class="price" viewBox="0 0 90 90" aria-label="$499">
      <polygon fill="var(--price-blue)" stroke="#1d3f8a" stroke-width="1" points="89,45 82.3,52.4 85.7,61.9 76.6,66.1 76.1,76.1 66.1,76.6 61.9,85.7 52.4,82.3 45,89 37.6,82.3 28.1,85.7 23.9,76.6 13.9,76.1 13.4,66.1 4.3,61.9 7.7,52.4 1,45 7.7,37.6 4.3,28.1 13.4,23.9 13.9,13.9 23.9,13.4 28.1,4.3 37.6,7.7 45,1 52.4,7.7 61.9,4.3 66.1,13.4 76.1,13.9 76.6,23.9 85.7,28.1 82.3,37.6"/>
      <text x="45" y="52" text-anchor="middle" font-size="22" fill="#ffffff">$499*</text>
    </svg>
    <p class="note">*plus sales tax &amp; shipping</p>
  </aside>

  <section class="testimonial">
    <blockquote>"Dale is someone who gets the job done. He is creative, trustworthy, and has an unusually well developed intellect."</blockquote>
    <cite>Warren Holt, Owner, Brookfield Services</cite>
  </section>

  <footer>
    <div class="band footer-band">All of this information is FREE to extremely LOW COST</div>
    <p class="copyright">© COPYRIGHT 2011 KRV/TNS Inc. All Rights Reserved.</p>
  </footer>
</body>
</html>
```